Corvanti, LLC Website

Creating website for medical billing company.

Target Market(s)

Medical providers

Industry/Entity Type

Medical billing

Coding

Coded - Design and coding required

Number of Pages Required

3 page

Font styles to use
Other font styles liked:
• Fonts that match our logo.

Requirements
Must have
• First page (greeting and explanation of who we are). Second page something about me and company (I'll supply some content, make generic for now). And page three, information that people can give for us to contact them.
Nice to have
• A little animation. But not over-the-top. Colors that match our logo.
Should not have
• Over-the-top animation.

```html
<!DOCTYPE html>
<html lang="en">
<head>
<meta charset="utf-8">
<title>Corvanti, LLC — Medical billing that keeps your practice paid</title>
<link href="https://fonts.googleapis.com/css2?family=Plus+Jakarta+Sans:wght@400;500;600;700;800&display=swap" rel="stylesheet">
<style>
:root{
  --navy:#1d3454;
  --ink:#24364f;
  --text:#5d6878;
  --muted:#8a93a0;
  --teal:#19b1cb;
  --slate:#2f4555;
  --band:#2e4a7b;
  --mist:#eff1f5;
  --line:#e3e6ec;
  --white:#ffffff;
}
*{box-sizing:border-box;margin:0;padding:0}
html,body{width:1200px;height:3943px;overflow:hidden}
body{font-family:"Plus Jakarta Sans",Arial,sans-serif;color:var(--ink);background:var(--white);position:relative}
a{color:inherit;text-decoration:none}
.abs{position:absolute}
.photo{position:absolute}

/* header + hero */
.hero{position:absolute;left:0;top:0;width:1200px;height:455px}
.hero .photo{inset:0;background:linear-gradient(100deg,#7fa6a0 0%,#a7b5b4 30%,#c8cdd0 48%,#d6d9dc 70%,#dcdfe2 100%)}
.site-header{position:absolute;left:207px;top:0;width:787px;height:92px;background:var(--white);z-index:2}
.topbar{position:absolute;left:27px;top:8px;right:27px;height:14px;display:flex;align-items:center;font-size:8.5px;color:var(--muted);white-space:nowrap}
.topbar .dot{width:12px;height:12px;border-radius:50%;background:var(--teal);margin-right:14px;flex:none}
.topbar .dot:nth-child(3){background:#2b6fa8}
.topbar .note{margin-left:6px}
.topbar .links{margin-left:auto;display:flex;gap:18px;align-items:center;color:var(--ink)}
.brand{position:absolute;left:27px;top:44px;display:flex;align-items:center;gap:9px;font-size:22px;font-weight:600;color:var(--navy);letter-spacing:-.3px;white-space:nowrap}
.brand .mark{width:26px;height:26px;background:var(--navy);border-radius:3px}
.nav{position:absolute;left:297px;top:44px;display:flex;align-items:flex-end;gap:30px;white-space:nowrap}
.nav .home{width:20px;height:20px;margin-right:16px}
.nav .item small{display:block;font-size:7px;letter-spacing:.8px;color:var(--muted);font-weight:600;margin-bottom:2px}
.nav .item span{font-size:16px;font-weight:700;color:var(--navy)}
.menu-btn{position:absolute;right:34px;top:46px;width:28px;height:28px;background:var(--teal);display:flex;flex-direction:column;justify-content:center;align-items:center;gap:3px}
.menu-btn i{display:block;width:12px;height:2px;background:#fff}
.hero-copy{position:absolute;left:609px;top:180px;width:340px}
.hero-copy p.kicker{font-size:14px;color:var(--ink)}
.hero-copy h1{font-size:56px;font-weight:800;color:var(--navy);letter-spacing:-1px;line-height:1;margin-top:6px;white-space:nowrap}
.hero-copy p.lead{font-size:11px;color:var(--text);line-height:1.7;margin-top:16px;width:300px}
.btn-light{display:flex;align-items:center;justify-content:center;width:231px;height:35px;background:#fff;color:var(--navy);font-size:9.5px;font-weight:700;letter-spacing:.8px;margin-top:28px;box-shadow:0 2px 6px rgba(0,0,0,.06)}

.contact-strip{position:absolute;left:0;top:455px;width:1200px;height:73px;border-bottom:1px solid var(--line)}
.contact-strip .lead{position:absolute;left:234px;top:28px;font-size:14px;color:var(--ink)}
.contact-strip .ways{position:absolute;right:234px;top:30px;display:flex;gap:36px;font-size:9px;color:var(--text);align-items:center;white-space:nowrap}
.contact-strip .ways span{display:flex;align-items:center;gap:8px}
.contact-strip b{color:var(--navy);text-decoration:underline}

/* section heads */
.label{display:flex;align-items:center;gap:8px;font-size:8.5px;font-weight:700;letter-spacing:.4px;color:var(--teal);text-transform:uppercase;white-space:nowrap}
.label::before{content:"";width:18px;height:11px;border-radius:6px;background:linear-gradient(90deg,var(--teal) 50%,var(--navy) 50%)}
.label.dark{color:var(--navy)}
.sec-title{font-size:32px;font-weight:700;line-height:1.15;color:var(--navy);letter-spacing:-.4px;white-space:nowrap}
.sec-intro{font-size:10px;color:var(--text);line-height:1.65;width:352px}
.sec-links{display:flex;gap:38px;align-items:center;font-size:10px;font-weight:600;color:var(--navy);margin-top:18px}
.go{display:inline-flex;width:22px;height:22px;border-radius:50%;background:var(--teal);align-items:center;justify-content:center;margin-left:8px;vertical-align:middle}
.sec-links span{display:flex;align-items:center}

.mist-band{position:absolute;left:0;top:888px;width:1200px;height:885px;background:var(--mist)}

.care-card{position:absolute;top:703px;width:357px;height:231px}
.care-card .photo{inset:0}
.care-tag{position:absolute;left:23px;top:111px;width:144px;height:97px;background:#fff;padding:20px 20px}
.care-tag b{display:block;font-size:19px;color:var(--teal);font-weight:800}
.care-tag span{display:block;font-size:9.5px;font-weight:700;color:var(--navy);margin-top:10px;line-height:1.35}
.pager{position:absolute;display:flex;gap:11px}
.pager i{display:block;width:68px;height:3px;background:#d5d9e0}
.pager i.on{background:var(--band)}

.excellence{position:absolute;left:0;top:1030px;width:1200px;text-align:center}
.excellence h2{font-size:21px;font-weight:700;color:var(--navy);line-height:1.3;letter-spacing:-.2px}
.excellence .cta{display:flex;justify-content:center;align-items:center;margin-top:12px;font-size:8.5px;font-weight:700;color:var(--teal);letter-spacing:.4px}

.svc{position:absolute;width:187px;padding-left:26px}
.svc svg{display:block;width:40px;height:40px}
.svc h3{font-size:13px;font-weight:700;color:var(--navy);margin-top:18px;white-space:nowrap}
.svc p{font-size:9.5px;color:var(--muted);line-height:1.5;margin-top:10px;width:130px}
.svc-sep{position:absolute;width:1px;background:#dfe2e8}
.areas{position:absolute;left:796px;top:1153px;width:170px;background:#fff;box-shadow:0 4px 18px rgba(29,52,84,.1)}
.areas li{list-style:none;height:43px;display:flex;align-items:center;justify-content:space-between;padding:0 18px;font-size:10px;font-weight:600;color:var(--navy);border-bottom:1px solid #edf0f3}
.areas li i{width:18px;height:18px;border-radius:50%;background:#dfe3e8}

.rule{position:absolute;left:234px;width:732px;height:6px;background:var(--slate)}
.row-note{position:absolute;right:234px;font-size:9px;color:var(--muted);white-space:nowrap}

.faq-photo{left:234px;top:1542px;width:732px;height:294px;background:linear-gradient(90deg,#6e8b7c 0%,#a6b19a 30%,#b9b4a8 48%,#cfd2d4 70%,#d8dadc 100%)}
.faq{position:absolute;left:609px;top:1592px;width:294px;height:294px;background:var(--slate);color:#fff;padding:22px 30px}
.faq .q{display:flex;justify-content:space-between;font-size:10px;font-weight:700;height:41px;align-items:center;border-bottom:1px solid rgba(255,255,255,.12)}
.faq .q.open{border:none;height:auto;padding-top:8px}
.faq .a{font-size:9px;line-height:1.65;color:rgba(255,255,255,.7);padding:12px 0 14px;border-bottom:1px solid rgba(255,255,255,.12)}
.faq .q:last-child{border:none}
.footnote{position:absolute;left:234px;top:1863px;font-size:8px;color:var(--text)}
.footnote b{color:var(--navy)}

.doc{position:absolute;top:2071px;width:131px}
.doc .photo{position:relative;height:131px;background:linear-gradient(180deg,#e4e6e9,#cdd2d8)}
.doc h4{font-size:15px;font-weight:700;color:var(--navy);margin-top:22px;white-space:nowrap}
.doc p{font-size:7px;color:var(--muted);line-height:1.55;margin-top:10px;text-transform:uppercase;letter-spacing:.2px}

.blog{position:absolute;left:0;top:2378px;width:1200px;height:543px;background:var(--band);color:#fff}
.blog h2{position:absolute;left:0;width:1200px;top:58px;text-align:center;font-size:21px;font-weight:700;line-height:1.2}
.blog .cta{position:absolute;left:0;width:1200px;top:121px;display:flex;justify-content:center;align-items:center;font-size:8.5px;font-weight:700;letter-spacing:.4px}
.post-main{position:absolute;left:234px;top:171px;width:357px}
.post-main .photo{position:relative;height:178px;background:linear-gradient(135deg,#6c6f6c,#a7a9a4 60%,#c6c6c2)}
.post-main h3{font-size:15px;font-weight:700;line-height:1.35;margin-top:20px;width:320px}
.post{position:absolute;top:171px;width:170px}
.post .photo{position:relative;height:85px}
.post h3{font-size:10px;font-weight:700;line-height:1.45;margin-top:12px}
.post p{font-size:8.5px;line-height:1.6;color:rgba(255,255,255,.7);margin-top:12px}
.post .tag{display:inline-block;border:1px solid rgba(255,255,255,.7);font-size:6.5px;font-weight:700;padding:1px 4px;margin-top:14px;letter-spacing:.4px}
.pages{position:absolute;left:234px;top:469px;display:flex;gap:9px}
.pages i{width:24px;height:24px;border-radius:50%;border:1px solid rgba(255,255,255,.5);font-style:normal;font-size:8px;display:flex;align-items:center;justify-content:center}
.pages i.on{background:#fff;color:var(--band)}
.next{position:absolute;left:796px;top:470px;width:170px;height:23px;border-radius:12px;background:#fff;color:var(--band);font-size:8px;font-weight:700;display:flex;align-items:center;justify-content:center}

.vid{position:absolute;top:3099px;width:231px}
.vid .photo{position:relative;height:129px}
.vid .play{position:absolute;left:18px;bottom:18px;width:26px;height:26px;border-radius:50%;border:2px solid #fff}
.vid .play::after{content:"";position:absolute;left:9px;top:6px;border-left:8px solid #fff;border-top:5px solid transparent;border-bottom:5px solid transparent}
.vid blockquote{font-size:9.5px;color:var(--text);line-height:1.6;margin-top:22px}
.vid cite{display:block;font-style:normal;font-size:7px;color:var(--muted);margin-top:16px;letter-spacing:.3px}

.quick{position:absolute;left:234px;top:3440px;width:732px;height:52px;display:grid;grid-template-columns:repeat(4,1fr);border:1px solid var(--line)}
.quick a{display:flex;align-items:center;justify-content:center;font-size:15px;font-weight:700;color:var(--navy);border-right:1px solid var(--line)}
.quick a:last-child{border:none}

.footer{position:absolute;left:0;top:3546px;width:1200px;height:300px;background:var(--mist)}
.fcol{position:absolute;top:56px;font-size:9px;color:var(--text)}
.fcol h5{font-size:10px;font-weight:600;color:var(--navy);margin-bottom:16px}
.fcol li{list-style:none;line-height:22.5px}
.fcol h5.gap{margin-top:22px}
.fbrand{position:absolute;left:796px;top:54px;width:170px;text-align:center}
.fbrand .mark{display:block;width:36px;height:36px;background:var(--navy);border-radius:4px;margin:0 auto}
.fbrand b{display:block;font-size:24px;font-weight:600;color:var(--navy);margin-top:8px;letter-spacing:-.3px;white-space:nowrap}
.btn-navy{position:absolute;left:796px;top:179px;width:170px;height:29px;background:var(--band);color:#fff;font-size:9.5px;font-weight:700;display:flex;align-items:center;justify-content:center}
.btn-ghost{position:absolute;left:796px;top:220px;width:170px;height:29px;border:1px solid #cfd4db;background:#f6f7f9;color:var(--text);font-size:9.5px;display:flex;align-items:center;justify-content:center}

.bottom{position:absolute;left:0;top:3846px;width:1200px;height:97px;background:#fff}
.bottom .brand{position:absolute;left:234px;top:36px;font-size:17px}
.bottom .brand .mark{width:22px;height:22px}
.bottom .copy{position:absolute;left:455px;top:43px;font-size:8.5px;color:var(--muted)}
.bottom .up{position:absolute;left:938px;top:33px;width:28px;height:28px;border-radius:50%;background:#e8ebef;display:flex;align-items:center;justify-content:center}
</style>
</head>
<body>

<section class="hero">
  <div class="photo" role="img" aria-label="Photo of a clinician in teal scrubs treating a patient, representing the providers Corvanti bills for"></div>
  <header class="site-header">
    <div class="topbar">
      <i class="dot"></i><i class="dot"></i><i class="dot"></i>
      <span class="note">Now onboarding new practices for the 2024 billing year</span>
      <nav class="links"><a>Specialties</a><a>Billing Resources</a><a>Contact Us</a><a>Portal</a>
        <svg width="11" height="11" viewBox="0 0 12 12"><circle cx="5" cy="5" r="3.8" fill="none" stroke="#1d3454" stroke-width="1.5"/><path d="M8 8l3 3" stroke="#1d3454" stroke-width="1.5"/></svg>
        <svg width="11" height="12" viewBox="0 0 11 12"><rect x="1" y="3" width="9" height="8" fill="none" stroke="#1d3454" stroke-width="1.4"/><path d="M3.5 3V1.5h4V3" fill="none" stroke="#1d3454" stroke-width="1.4"/></svg>
      </nav>
    </div>
    <a class="brand"><i class="mark"></i>Corvanti, LLC</a>
    <nav class="nav">
      <svg class="home" viewBox="0 0 20 20"><path d="M2 10L10 2l8 8v8h-5v-5H7v5H2z" fill="#19b1cb"/></svg>
      <a class="item"><small>WHO WE ARE</small><span>About us ⌄</span></a>
      <a class="item"><small>WHAT WE HANDLE</small><span>Services ⌄</span></a>
      <a class="item"><small>TALK TO OUR TEAM</small><span>Contact us</span></a>
    </nav>
    <a class="menu-btn" aria-label="Menu"><i></i><i></i><i></i></a>
  </header>
  <div class="hero-copy">
    <p class="kicker">Getting your practice paid is</p>
    <h1>our priority</h1>
    <p class="lead">Accurate coding, clean claims and steady follow-up so you can focus on patients, not paperwork.</p>
    <a class="btn-light">GET STARTED</a>
  </div>
</section>

<section class="contact-strip">
  <p class="lead">Contact our billing experts via either phone or email</p>
  <div class="ways">
    <span><svg width="14" height="12" viewBox="0 0 14 12"><path d="M2 4c0-2 10-2 10 0v1H9V4H5v1H2z M3 7h8v4H3z" fill="#19b1cb"/></svg>Give us a call <b>0700 555 0142</b></span>
    <span><svg width="14" height="11" viewBox="0 0 14 11"><rect x="0.5" y="0.5" width="13" height="10" fill="none" stroke="#19b1cb"/><path d="M1 1l6 5 6-5" fill="none" stroke="#19b1cb"/></svg>Email our experts <b>Ask a question</b></span>
  </div>
</section>

<div class="mist-band"></div>

<section class="about">
  <div class="abs label" style="left:234px;top:576px">Who we are and what we do</div>
  <h2 class="abs sec-title" style="left:234px;top:594px">We’re committed to<br>your revenue cycle</h2>
  <div class="abs" style="left:609px;top:572px">
    <p class="sec-intro">We provide medical billing, coding and claims management for practices of every size. We promise to handle every claim with care, and to keep your collections steady and on time.</p>
    <div class="sec-links"><a>Learn more about us</a><span>Send us a Message<i class="go"><svg width="9" height="8" viewBox="0 0 9 8"><path d="M0 4h7M4 1l3 3-3 3" stroke="#fff" fill="none" stroke-width="1.4"/></svg></i></span></div>
  </div>
  <article class="care-card" style="left:234px">
    <div class="photo" role="img" aria-label="Photo of a billing consultant in a blazer meeting with a provider" style="background:linear-gradient(100deg,#e3e3e0,#cfc8c0 55%,#e6e6e4)"></div>
    <div class="care-tag"><b>1.</b><span>Medical Billing &amp;<br>Claims Submission</span></div>
  </article>
  <article class="care-card" style="left:609px">
    <div class="photo" role="img" aria-label="Photo of a coder reviewing patient records by green plants" style="background:linear-gradient(100deg,#6f8a69,#aab5a0 45%,#e4e1dc)"></div>
    <div class="care-tag"><b>2.</b><span>Medical Coding &amp;<br>Chart Review</span></div>
  </article>
  <div class="pager" style="left:487px;top:980px"><i class="on"></i><i></i><i></i></div>
</section>

<section class="excellence">
  <h2>Known for accurate, on-time billing,<br>Below is a list of some of the services provided</h2>
  <div class="cta">BILLING SERVICES AND SPECIALTIES<i class="go"><svg width="9" height="8" viewBox="0 0 9 8"><path d="M0 4h7M4 1l3 3-3 3" stroke="#fff" fill="none" stroke-width="1.4"/></svg></i></div>
</section>

<section class="services">
  <div class="svc" style="left:234px;top:1153px">
    <svg viewBox="0 0 40 40"><rect x="8" y="4" width="22" height="30" rx="2" fill="#9aa3ae"/><path d="M13 12h12M13 18h12M13 24h7" stroke="#fff" stroke-width="2"/><circle cx="30" cy="30" r="7" fill="#19b1cb"/><path d="M27 30l2 2 4-4" stroke="#fff" stroke-width="1.8" fill="none"/></svg>
    <h3>Claims Submission</h3><p>Clean claims sent fast to every major payer.</p>
  </div>
  <div class="svc" style="left:421px;top:1153px">
    <svg viewBox="0 0 40 40"><rect x="5" y="8" width="30" height="24" rx="2" fill="#9aa3ae"/><path d="M12 16l-4 4 4 4M28 16l4 4-4 4" stroke="#19b1cb" stroke-width="2.5" fill="none"/></svg>
    <h3>Medical Coding</h3><p>Certified coders for accurate CPT and ICD-10.</p>
  </div>
  <div class="svc" style="left:608px;top:1153px">
    <svg viewBox="0 0 40 40"><circle cx="20" cy="6" r="3" fill="#19b1cb"/><circle cx="28" cy="10" r="2.5" fill="#19b1cb"/><circle cx="13" cy="11" r="2" fill="#19b1cb"/><path d="M4 26c6-2 12 2 18 0l10-4v6L20 34H4z" fill="#9aa3ae"/></svg>
    <h3>Payment Posting</h3><p>Every payment posted and reconciled daily.</p>
  </div>
  <div class="svc" style="left:234px;top:1298px">
    <svg viewBox="0 0 40 40"><circle cx="20" cy="20" r="14" fill="#9aa3ae"/><path d="M12 20h16M20 12v16" stroke="#19b1cb" stroke-width="3" transform="rotate(45 20 20)"/></svg>
    <h3>Denial Management</h3><p>We work denials and appeals to recover revenue.</p>
  </div>
  <div class="svc" style="left:421px;top:1298px">
    <svg viewBox="0 0 40 40"><path d="M4 6h18v12c0 6-4 10-9 10S4 24 4 18z" fill="#9aa3ae"/><path d="M20 14h16v12c0 6-4 9-8 9s-8-3-8-9z" fill="#19b1cb"/></svg>
    <h3>Credentialing</h3><p>Payer enrollment handled from start to finish.</p>
  </div>
  <div class="svc" style="left:608px;top:1298px">
    <svg viewBox="0 0 40 40"><rect x="6" y="22" width="6" height="12" fill="#9aa3ae"/><rect x="17" y="14" width="6" height="20" fill="#9aa3ae"/><rect x="28" y="6" width="6" height="28" fill="#19b1cb"/></svg>
    <h3>Revenue Reporting</h3><p>Clear monthly reports on your collections.</p>
  </div>
  <div class="svc-sep" style="left:420px;top:1153px;height:262px"></div>
  <div class="svc-sep" style="left:607px;top:1153px;height:262px"></div>
  <ul class="areas">
    <li>Family Medicine<i></i></li><li>Pediatrics<i></i></li><li>Behavioral Health<i></i></li><li>Orthopedics<i></i></li><li>Physical Therapy<i></i></li><li style="border:none">Radiology<i></i></li>
  </ul>
</section>

<section class="faq-section">
  <div class="rule" style="top:1465px"></div>
  <div class="abs label dark" style="left:234px;top:1494px">Frequently asked questions about billing</div>
  <p class="row-note" style="top:1494px">Billing FAQs: Short answers to common questions</p>
  <div class="photo faq-photo" role="img" aria-label="Photo of a smiling provider greeting a colleague"></div>
  <div class="faq">
    <div class="q open"><span>What does a billing partner do?</span><span>×</span></div>
    <p class="a">We code visits, submit claims, post payments and chase denials, so your practice is paid in full and on time…</p>
    <div class="q"><span>How fast are claims submitted?</span><span>+</span></div>
    <div class="q"><span>Which specialties do you bill for?</span><span>+</span></div>
    <div class="q"><span>How is your fee calculated?</span><span>+</span></div>
    <div class="q"><span>How do I get started?</span><span>+</span></div>
  </div>
  <p class="footnote">** FAQ adapted from the <b>Provider Billing Standards Guide.</b></p>
</section>

<section class="team">
  <div class="abs label" style="left:234px;top:1949px">Meet our team</div>
  <h2 class="abs sec-title" style="left:234px;top:1967px">Following is our<br>team of specialists</h2>
  <div class="abs" style="left:609px;top:1944px">
    <p class="sec-intro">We are a group of certified coders and billing specialists who came together with one goal - to give medical providers billing they never have to worry about.</p>
    <div class="sec-links"><a>Learn more about us</a><span>Send us a Message<i class="go"><svg width="9" height="8" viewBox="0 0 9 8"><path d="M0 4h7M4 1l3 3-3 3" stroke="#fff" fill="none" stroke-width="1.4"/></svg></i></span></div>
  </div>
  <div class="doc" style="left:234px"><div class="photo" role="img" aria-label="Portrait of the company founder"></div><h4>Amara Osei</h4><p>Founder and owner,<br>director of billing</p></div>
  <div class="doc" style="left:384px"><div class="photo" role="img" aria-label="Portrait of a senior coding specialist"></div><h4>Elwin Harte</h4><p>Certified professional<br>coder, team lead</p></div>
  <div class="doc" style="left:534px"><div class="photo" role="img" aria-label="Portrait of a claims specialist"></div><h4>Selina Voss</h4><p>Claims and denial<br>management specialist</p></div>
  <div class="doc" style="left:684px"><div class="photo" role="img" aria-label="Portrait of a credentialing coordinator"></div><h4>Mrs. Petra</h4><p>Credentialing and payer<br>enrollment coordinator</p></div>
  <div class="doc" style="left:835px"><div class="photo" role="img" aria-label="Portrait of an accounts specialist"></div><h4>Ravi Kanth</h4><p>Payment posting and<br>revenue reporting</p></div>
  <div class="pager" style="left:527px;top:2322px"><i class="on"></i><i></i></div>
</section>

<section class="blog">
  <h2>Articles, tips and resources you can access<br>for free to help your practice……Right Now!</h2>
  <div class="cta">EXPLORE ALL BLOG POSTS<i class="go"><svg width="9" height="8" viewBox="0 0 9 8"><path d="M0 4h7M4 1l3 3-3 3" stroke="#fff" fill="none" stroke-width="1.4"/></svg></i></div>
  <article class="post-main">
    <div class="photo" role="img" aria-label="Photo of a speaker training a small seated group"></div>
    <h3>Cutting claim denials in your everyday practice</h3>
  </article>
  <article class="post" style="left:609px">
    <div class="photo" role="img" aria-label="Photo of a frustrated man against a red background" style="background:linear-gradient(135deg,#d8432c,#e9735a 60%,#c9342a)"></div>
    <h3>Can better coding stop underpayments?</h3>
    <p>Small coding errors quietly cost practices thousands each year, and most go unnoticed until…</p>
    <span class="tag">CODING</span>
  </article>
  <article class="post" style="left:796px">
    <div class="photo" role="img" aria-label="Photo of a group of adults in a bright studio" style="background:linear-gradient(135deg,#8fb3a8,#b9cbbf 50%,#7c9d92)"></div>
    <h3>In-house or outsourced billing: which is right?</h3>
    <p>It’s long been debated whether keeping billing in-house is worth the cost for…</p>
    <span class="tag">PRACTICE</span>
  </article>
  <div class="pages"><i class="on">1</i><i>2</i><i>3</i></div>
  <a class="next">Next »</a>
</section>

<section class="testimonials">
  <div class="abs label" style="left:234px;top:2975px">What providers and practice managers say</div>
  <h2 class="abs sec-title" style="left:234px;top:2994px">What providers and<br>practice managers say</h2>
  <div class="abs" style="left:609px;top:2970px">
    <p class="sec-intro">Here is a few testimonials and feedback from practices we bill for, from solo clinics to group practices. Most came from review calls and end of year check-ins.</p>
    <div class="sec-links"><a>Learn more about us</a><span>Send us a Message<i class="go"><svg width="9" height="8" viewBox="0 0 9 8"><path d="M0 4h7M4 1l3 3-3 3" stroke="#fff" fill="none" stroke-width="1.4"/></svg></i></span></div>
  </div>
  <article class="vid" style="left:234px">
    <div class="photo" role="img" aria-label="Video still of a provider sitting on a sofa by plants" style="background:linear-gradient(135deg,#6f7c68,#a9a79c 55%,#8b8d86)"><i class="play"></i></div>
    <blockquote>“Our collections went up within three months. I finally stopped worrying about claims and spend my time with patients.”</blockquote>
    <cite>DR ALEX MARLOW – FAIRMONT, EASTVALE</cite>
  </article>
  <article class="vid" style="left:484px">
    <div class="photo" role="img" aria-label="Video still of a practice manager speaking in a bright room" style="background:linear-gradient(135deg,#c9ccc9,#9a9d9a 55%,#d9dad8)"><i class="play"></i></div>
    <blockquote>“Daniel and the team cleared our backlog of denials… I recommend Corvanti to every practice I know.”</blockquote>
    <cite>DR SAMIR – CLIENT</cite>
  </article>
  <article class="vid" style="left:735px">
    <div class="photo" role="img" aria-label="Video still of an office manager talking in a room with plants" style="background:linear-gradient(135deg,#7b8a72,#b7b4a9 55%,#8c9185)"><i class="play"></i></div>
    <blockquote>“Clear reports every month and a team that answers the phone. They have made a real difference for our clinic.”</blockquote>
    <cite>HELEN BROOKS – FAIRMONT, EASTVALE</cite>
  </article>
</section>

<section class="quicklinks">
  <div class="rule" style="top:3366px"></div>
  <div class="abs label dark" style="left:234px;top:3396px">Quick links to the information</div>
  <p class="row-note" style="top:3396px">Any questions? We can help!</p>
  <nav class="quick"><a>Client Portal</a><a>Pay my Bill</a><a>Staff Portal</a><a>Career</a></nav>
</section>

<footer class="footer">
  <div class="fcol" style="left:234px">
    <h5>Corvanti headquarters</h5>
    <ul><li>Harborview, Northstate 4410</li><li>Toll-free: +1.800.555.0199</li><li>Fax: +1.610.555.0127</li></ul>
    <h5 class="gap">Find us on social media</h5>
    <ul><li>Microblog</li><li>Social Feed</li><li>Pro Network</li></ul>
  </div>
  <div class="fcol" style="left:421px">
    <h5>Billing Services</h5>
    <ul><li>Claims submission</li><li>Medical coding</li><li>Payment posting</li><li>Denial management</li><li>Credentialing</li><li>Revenue reporting</li><li>Patient statements</li><li>All billing services</li></ul>
  </div>
  <div class="fcol" style="left:609px">
    <h5>Quick links &amp; informations</h5>
    <ul><li>Company profile</li><li>Client reviews</li><li>Ethics and compliance</li><li>Licenses and certificates</li><li>Meet our team</li><li>Mission and core value</li><li>News and media</li><li>Questions and answers</li></ul>
  </div>
  <div class="fbrand"><i class="mark"></i><b>Corvanti, LLC</b></div>
  <a class="btn-navy">Request a Callback</a>
  <a class="btn-ghost">Get a Quote</a>
</footer>

<div class="bottom">
  <a class="brand"><i class="mark"></i>Corvanti, LLC</a>
  <p class="copy">Copyright © 2023 Corvanti LLC. All Rights Reserved. Terms &amp; Conditions | Privacy Policy.</p>
  <a class="up" aria-label="Back to top"><svg width="9" height="10" viewBox="0 0 9 10"><path d="M4.5 10V1M1 4.5l3.5-3.5L8 4.5" fill="none" stroke="#1d3454" stroke-width="1.4"/></svg></a>
</div>

</body>
</html>
```